FotoVELTA buisnesscard

Hey :) I need a modern buisnesscard for my company FotoVELTA
It most have:
Dagligleder og Fotograf: Henrik Torvald Bjelland

Mob: +4791642058
Epost: post@fotovelta.no
Adresse: Bakkestien22, 6030 Langevåg

Facbook and instagram logo with text FotoVELTA

FotoVELTA logo

It Company

```html
<!DOCTYPE html>
<html lang="no">
<head>
<meta charset="utf-8">
<title>FotoVELTA – visittkort</title>
<link href="https://fonts.googleapis.com/css2?family=Open+Sans:wght@400;600;700&display=swap" rel="stylesheet">
<style>
  :root {
    --bg: #3a3b3d;
    --brand-blue: #1174bb;
    --brand-pink: #c2437f;
    --paper: #ffffff;
    --ink: #3c3c3c;
    --rule: #8a8a8a;
  }
  html, body {
    margin: 0;
    width: 1200px;
    height: 1200px;
    overflow: hidden;
    background: var(--bg);
    font-family: "Open Sans", Arial, sans-serif;
  }
  .canvas {
    position: relative;
    width: 1200px;
    height: 1200px;
  }
  .card {
    position: absolute;
    left: 180px;
    width: 840px;
    height: 480px;
    border-radius: 28px;
    overflow: hidden;
    box-shadow: 0 14px 30px rgba(0,0,0,.45);
  }
  .card-front { top: 90px; background: var(--brand-blue); }
  .card-back { top: 630px; background: var(--paper); }

  .card-shapes { position: absolute; inset: 0; }

  .front-logo {
    position: absolute;
    left: 0; right: 0; top: 180px;
    text-align: center;
    color: var(--paper);
    font-weight: 700;
    font-size: 72px;
    letter-spacing: 1px;
  }

  .back-logo {
    position: absolute;
    left: 50px; top: 196px;
    width: 330px;
    text-align: center;
    color: var(--brand-blue);
    font-weight: 700;
    font-size: 52px;
    letter-spacing: .5px;
  }

  .divider {
    position: absolute;
    left: 400px; top: 70px;
    width: 2px; height: 240px;
    background: var(--rule);
  }

  .contact {
    position: absolute;
    left: 440px; top: 60px;
    color: var(--ink);
  }
  .contact-name {
    margin: 0;
    color: var(--brand-blue);
    font-weight: 700;
    font-size: 27px;
  }
  .contact-title {
    margin: 2px 0 24px;
    color: var(--brand-pink);
    font-size: 20px;
  }
  .contact-address {
    margin: 0 0 20px;
    font-size: 19px;
    line-height: 1.3;
  }
  .contact-list { list-style: none; margin: 0; padding: 0; font-size: 19px; line-height: 1.45; }
  .contact-list li { display: flex; align-items: center; gap: 12px; }
  .contact-list svg { width: 16px; height: 16px; flex: none; }
</style>
</head>
<body>
<main class="canvas">

  <section class="card card-front" aria-label="Forside">
    <svg class="card-shapes" viewBox="0 0 840 480" preserveAspectRatio="none" aria-hidden="true">
      <rect x="0" y="446" width="840" height="34" fill="var(--brand-pink)"/>
    </svg>
    <div class="front-logo">FotoVELTA</div>
  </section>

  <section class="card card-back" aria-label="Bakside">
    <svg class="card-shapes" viewBox="0 0 840 480" preserveAspectRatio="none" aria-hidden="true">
      <polygon points="0,444 496,444 488,480 0,480" fill="var(--brand-pink)"/>
      <polygon points="516,404 840,404 840,480 498,480" fill="var(--brand-blue)"/>
    </svg>

    <div class="back-logo">FotoVELTA</div>

    <div class="divider"></div>

    <div class="contact">
      <p class="contact-name">Henrik Torvald Bjelland</p>
      <p class="contact-title">Dagligleder og Fotograf</p>
      <p class="contact-address">Bakkestien22,<br>6987 Bjørkavik</p>
      <ul class="contact-list">
        <li>
          <svg viewBox="0 0 16 16"><path d="M4 1l3 3-2 2c1 2 3 4 5 5l2-2 3 3-2 3C7 15 1 9 1 3z" fill="var(--brand-blue)"/></svg>
          +4791642058
        </li>
        <li>
          <svg viewBox="0 0 16 16"><rect x="1" y="3" width="14" height="10" fill="var(--brand-blue)"/><path d="M1 3l7 6 7-6" stroke="#fff" stroke-width="1.5" fill="none"/></svg>
          post@fotovelta.no
        </li>
        <li>
          <svg viewBox="0 0 16 16"><rect x="1" y="1" width="14" height="14" rx="2" fill="var(--brand-blue)"/></svg>
          /FotoVELTA
        </li>
        <li>
          <svg viewBox="0 0 16 16"><rect x="1" y="1" width="14" height="14" rx="2" fill="var(--brand-blue)"/></svg>
          @FotoVELTA
        </li>
      </ul>
    </div>
  </section>

</main>
</body>
</html>
```